Packaging design for HOT NEW RETAIL BEARD OIL BRAND - Merrow Fennick Apothecary

Packaging design for beard oils. I've attached a brief, and I've also attached a few examples of bottles and boxes. Of course, we need an entirely unique look. I've attached the photo of Merrow Fennick as well - you can choose to use it or not (I'm open).

This product will be sold at national retailers and needs to look like a brand that is sold at boutique

What the consumer wants to see on the shelf:
-Box should larger than others and be soft touch (feels luxurious)
-More “hipster look/feel”
-Text should stand out like inspiration photos - jumping off the shelf to the consumer
-Use the existing logo of Merrow Fennick
-Deco will be wrap label as shown in current product image
-Sample text to pull copy for outer carton (taken from label on glass bottle):
-Strengthen and condition your beard with this blend of natural oils. Sunflower oil is rich in omega, fatty acids and vitamins E, C, B, and A, while avocado oil hydrates the beard fibers from root to tip, keep the beard looking and feeling extraordinary. Smooth into your beard for a healthy sheen and a woodsy scent evoking the great outdoors.
-Cool/Hipster product at discount pricing

Target Market(s)

Men from ages 20-40. Women also buy this product for their men, so it needs to look like a well known brand.

Industry/Entity Type

Hair And Beauty

Font styles to use
Sans Serif

Colors

Designer to choose colors to be used in the design.

Requirements
Must have
• A full label and box design with key call outs:
• Features and benefits - found in attached brief
• Description of what it is: Beard Oil
• Name of frangrance: Sandalwood
• Size: 2 oz / 60 ml
Nice to have
• Feel free to revamp the logo if needed. I am not married to the font for Merrow Fennick Apothecary.

```html
<!DOCTYPE html>
<html lang="en">
<head>
<meta charset="UTF-8">
<title>Merrow Fennick Apothecary – Softening Beard Oil Labels</title>
<link href="https://fonts.googleapis.com/css2?family=Oswald:wght@400;500;600;700&family=Libre+Baskerville&family=Montserrat:wght@300&display=swap" rel="stylesheet">
<style>
  :root {
    --backdrop: #e3e3e3;
    --label-black: #151515;
    --ink-white: #f4f4f2;
    --cream: #e9e7e1;
    --cream-ink: #1a1a1a;
    --muted: #bdbdbd;
    --pattern-tone: #5a5a5a;
  }
  * { box-sizing: border-box; margin: 0; padding: 0; }
  html, body {
    width: 1200px; height: 900px; overflow: hidden;
    background: var(--backdrop);
  }
  .canvas { position: relative; width: 1200px; height: 900px; }

  .label {
    position: absolute; top: 170px;
    width: 400px; height: 540px;
    background: var(--label-black);
    color: var(--ink-white);
  }
  .label--front { left: 160px; }
  .label--back  { left: 640px; }

  /* frame */
  .frame {
    position: absolute; left: 38px; right: 38px;
    border: 2px solid var(--ink-white);
  }
  .label--front .frame { top: 112px; bottom: 62px; }
  .label--back  .frame { top: 88px; bottom: 62px; }

  /* brand mark stand-in */
  .brand-mark {
    position: absolute; left: 50%; transform: translateX(-50%);
    background: var(--label-black);
    display: flex; flex-direction: column; align-items: center;
    padding: 0 14px;
  }
  .label--front .brand-mark { top: 40px; }
  .label--back  .brand-mark { top: 26px; }
  .brand-mark__circle {
    border: 2px solid var(--ink-white); border-radius: 50%;
    display: flex; align-items: center; justify-content: center;
    text-align: center;
    font-family: 'Oswald', sans-serif; font-weight: 500;
    text-transform: uppercase; color: var(--ink-white);
  }
  .label--front .brand-mark__circle { width: 118px; height: 118px; font-size: 13px; line-height: 1.25; letter-spacing: 0.06em; }
  .label--back  .brand-mark__circle { width: 76px; height: 76px; font-size: 8.5px; line-height: 1.25; letter-spacing: 0.05em; }

  /* front content */
  .brand-name {
    position: absolute; top: 176px; left: 0; right: 0;
    text-align: center; font-family: 'Oswald', sans-serif;
    text-transform: uppercase; line-height: 1;
  }
  .brand-name__main { display: block; font-size: 21px; font-weight: 500; letter-spacing: 0.01em; }
  .brand-name__sub { display: block; font-size: 12px; font-weight: 500; margin-top: 3px; }

  .product-panel {
    position: absolute; top: 232px; left: 38px; right: 38px; height: 128px;
    background: var(--cream); color: var(--cream-ink);
  }
  .product-panel__box {
    position: absolute; top: 22px; left: 20px; right: 20px; bottom: 18px;
    border: 2px solid var(--cream-ink);
    display: flex; align-items: center; justify-content: center;
  }
  .product-panel__tag {
    position: absolute; top: 8px; left: 50%; transform: translateX(-50%);
    background: var(--label-black); color: var(--ink-white);
    font-family: 'Libre Baskerville', serif; font-size: 17px; letter-spacing: 0.06em;
    padding: 1px 8px 2px; text-transform: uppercase; white-space: nowrap;
  }
  .product-panel__title {
    font-family: 'Oswald', sans-serif; font-weight: 700;
    font-size: 58px; line-height: 1; text-transform: uppercase; margin-top: 8px;
    letter-spacing: -0.01em;
  }

  .claims {
    position: absolute; top: 360px; left: 38px; width: 190px; height: 118px;
    padding: 10px 4px 0 8px;
    font-family: 'Oswald', sans-serif; text-transform: uppercase; line-height: 1.2;
  }
  .claims__lead { font-size: 14px; font-weight: 600; }
  .claims__detail { font-size: 8.5px; font-weight: 500; }
  .claims__vitamins { font-size: 15.5px; font-weight: 600; margin-top: 2px; }

  .scent {
    position: absolute; top: 360px; right: 38px; width: 124px; height: 118px;
    border-left: 2px solid var(--ink-white);
  }
  .scent__pattern {
    position: absolute; inset: 0;
    background: linear-gradient(160deg, #6b6b6b 0%, var(--pattern-tone) 55%, #3e3e3e 100%);
  }
  .scent__name {
    position: absolute; inset: 0;
    display: flex; flex-direction: column; align-items: flex-end; justify-content: center;
    padding-right: 8px;
    font-family: 'Oswald', sans-serif; font-weight: 600; font-size: 30px;
    line-height: 1.08; text-transform: uppercase; letter-spacing: 0.04em;
  }

  .net-volume {
    position: absolute; bottom: 28px; left: 0; right: 0; text-align: center;
    font-family: 'Montserrat', sans-serif; font-weight: 300; font-size: 14px; color: var(--muted);
  }

  /* back content */
  .copy {
    position: absolute; top: 146px; left: 62px; right: 62px;
    font-family: 'Libre Baskerville', serif; font-size: 13px; line-height: 1.38;
    color: var(--ink-white);
  }
  .copy__intro { text-align: center; letter-spacing: 0.02em; margin-bottom: 14px; }
  .copy__heading { margin-top: 8px; }
  .copy__text { margin-top: 5px; }
  .copy__direction { margin-top: 12px; }
  .moustache-spot {
    position: absolute; bottom: 92px; left: 50%; transform: translateX(-50%);
    width: 40px; height: 10px; border-radius: 5px; background: var(--ink-white);
  }
</style>
</head>
<body>
<main class="canvas">

  <section class="label label--front" aria-label="Front label">
    <div class="frame"></div>
    <div class="brand-mark">
      <div class="brand-mark__circle">Merrow<br>Fennick<br>Apothecary</div>
    </div>
    <h2 class="brand-name">
      <span class="brand-name__main">Merrow Fennick</span>
      <span class="brand-name__sub">Apothecary</span>
    </h2>
    <div class="product-panel">
      <div class="product-panel__box">
        <h1 class="product-panel__title">Beard Oil</h1>
      </div>
      <span class="product-panel__tag">Softening</span>
    </div>
    <div class="claims">
      <p class="claims__lead">Strengthen and condition</p>
      <p class="claims__detail">Your beard with this blend of natural oils<br>Sunflower oil &amp; avocado oil</p>
      <p class="claims__vitamins">Vitamins E, C, B, and A</p>
    </div>
    <div class="scent">
      <div class="scent__pattern" role="img" aria-label="Flowing wave line pattern in grey tones"></div>
      <p class="scent__name"><span>Cool</span><span>Breeze</span></p>
    </div>
    <p class="net-volume">60 ml / 2 fl oz</p>
  </section>

  <section class="label label--back" aria-label="Back label">
    <div class="frame"></div>
    <div class="brand-mark">
      <div class="brand-mark__circle">Merrow<br>Fennick<br>Apothecary</div>
    </div>
    <div class="copy">
      <p class="copy__intro">Keep the beard looking and feeling extraordinary. Smooth into your beard for a healthy sheen and a woodsy scent evoking the great outdoors.</p>
      <p class="copy__heading">Sunflower oil</p>
      <p class="copy__text">Is rich in Omega, fatty acids and vitamins E, C, B and A</p>
      <p class="copy__heading">Avocado oil</p>
      <p class="copy__text">Hydrates the beard fibers from root to tip</p>
      <p class="copy__direction">Direction: Apply a small amount in your palm. Gently massage into the beard hair and underneath skin.</p>
    </div>
    <div class="moustache-spot" role="img" aria-label="Small moustache ornament"></div>
  </section>

</main>
</body>
</html>
```